Frozen Yogurt Website

I need a new website based in Sydney Pelham Wharf. Our products are:

Frozen Yogurt
Smoothies
Organic Acai Bowls / Smoothies

we have professional photos of gourmet fruit and toppings in high resolution
we have the logo
we just need a web designer

no ecommerce required. Just promotional website:

following pages are needed:

About Us
Contact Us
Frozen Yogurt
Toppings
Smoothies
Acai Bowls

examples of websites we like:
http://www.velmorastreet.com
http://myplentifulpantry.com.au/
http://www.brumo.com.au

any questions please feel free to ask
Updates

Target Market(s)

healthy and organic food lovers
Frozen yogurt / desert eaters
tourist in pelham wharf

Industry/Entity Type

Promotional

Requirements
Should not have
• no ecommerce required

```html
<!DOCTYPE html>
<html lang="en">
<head>
<meta charset="utf-8">
<title>Yovella – Authentic Frozen Yogurt</title>
<link rel="stylesheet" href="https://fonts.googleapis.com/css2?family=Lobster+Two:ital@1&family=Roboto+Condensed:ital,wght@0,400;0,700;1,400;1,700&display=swap">
<style>
  :root {
    --green-dark: #6f7d02;
    --green-mid: #8a9e04;
    --green-light: #b3c52a;
    --green-text: #c9d95a;
    --olive-ink: #5e6a08;
    --orange-top: #ff9c08;
    --orange-mid: #ff8f03;
    --orange-deep: #ff7a00;
    --ink-brown: #5b3a06;
    --white: #ffffff;
  }
  html, body {
    margin: 0;
    width: 1159px;
    height: 1200px;
    overflow: hidden;
  }
  body {
    position: relative;
    font-family: "Roboto Condensed", sans-serif;
    background: var(--orange-mid);
  }
  .abs { position: absolute; }
  .center-x { transform: translateX(-50%); white-space: nowrap; }

  /* header */
  .site-header {
    position: absolute; left: 0; top: 0; width: 1159px; height: 486px;
    background: linear-gradient(180deg, var(--green-dark) 0%, var(--green-mid) 45%, #88a003 75%, var(--green-dark) 100%);
  }
  .brand {
    position: absolute; left: 279px; top: 16px; width: 96px; height: 96px;
    border-radius: 50%; background: var(--white);
    box-shadow: 0 0 0 3px #c7d64b inset;
    display: flex; align-items: center; justify-content: center;
  }
  .brand-name {
    font-family: "Roboto Condensed", sans-serif; font-weight: 700;
    font-size: 24px; color: #3c3c3c;
  }
  .ownership { left: 573px; top: 32px; text-align: center; color: var(--white); }
  .ownership-figure { font-weight: 700; font-size: 32px; line-height: 1; }
  .ownership-label { font-size: 18px; text-decoration: underline; text-underline-offset: 3px; letter-spacing: .3px; }
  .delivery { left: 803px; top: 18px; text-align: center; }
  .delivery-label { color: var(--green-text); font-size: 17px; }
  .delivery-phone { color: var(--white); font-style: italic; font-size: 19px; letter-spacing: 1px; margin-top: 2px; }
  .delivery-rule { left: 727px; top: 68px; width: 153px; height: 1px; background: rgba(70,80,0,.45); box-shadow: 0 1px 0 rgba(200,220,80,.3); }
  .social { left: 773px; top: 79px; display: flex; gap: 5px; }
  .social span { width: 16px; height: 16px; border-radius: 3px; background: var(--green-text); }

  .slider-frame {
    left: 278px; top: 124px; width: 603px; height: 289px;
    border-radius: 10px; background: var(--green-light);
  }
  .slider-shadow {
    left: 330px; top: 408px; width: 500px; height: 24px; border-radius: 50%;
    background: radial-gradient(ellipse at center, rgba(90,100,0,.45), rgba(90,100,0,0) 70%);
  }
  .slide {
    left: 290px; top: 135px; width: 579px; height: 266px; border-radius: 6px;
    background: radial-gradient(ellipse at 50% 45%, #c6e00c 0%, #93ac05 40%, #5b6d03 100%);
  }
  .slide-arrow { width: 27px; height: 27px; }
  .main-nav, .footer-nav { display: flex; font-family: "Lobster Two", cursive; color: #3d3c06; }
  .main-nav { left: 0; top: 441px; width: 1159px; justify-content: center; gap: 26px; font-size: 15.5px; }

  /* welcome band */
  .welcome-band { left: 0; top: 486px; width: 1159px; height: 224px; background: var(--orange-top); }
  .script-title { font-family: "Lobster Two", cursive; color: var(--olive-ink); font-size: 23px; }
  .welcome-sub { font-style: italic; color: #8a5a04; font-size: 14px; }
  .taster {
    width: 90px; height: 90px; border-radius: 50%; background: #ff8a0a;
    display: flex; align-items: center; justify-content: center;
    box-shadow: 0 1px 2px rgba(160,70,0,.4);
  }
  .taster-photo { width: 78px; height: 78px; border-radius: 50%; }

  /* story band */
  .story-band { left: 0; top: 710px; width: 1159px; height: 362px; background: linear-gradient(180deg, var(--orange-mid), #ff8a02); }
  .band-shadow {
    left: 300px; width: 560px; height: 26px;
    background: radial-gradient(ellipse at 50% 0%, rgba(230,80,0,.55), rgba(230,80,0,0) 70%);
  }
  .copy {
    left: 279px; width: 602px; text-align: center; color: var(--ink-brown);
    font-style: italic; font-size: 12px; line-height: 18.3px;
  }
  .copy strong { display: block; font-style: italic; color: #3a2400; }
  .dot { display: inline-block; width: 4px; height: 4px; border-radius: 50%; background: #a76508; margin: 0 6px 2px; }

  .site-footer { left: 0; top: 1072px; width: 1159px; height: 128px; background: #ff8f00; }
  .footer-nav { left: 0; top: 1124px; width: 1159px; justify-content: center; gap: 11px; font-size: 12.5px; }
</style>
</head>
<body>
  <header class="site-header">
    <div class="brand"><span class="brand-name">yovella</span></div>

    <div class="abs ownership center-x">
      <div class="ownership-figure">100%</div>
      <div class="ownership-label">AUSTRALIAN OWNED</div>
    </div>

    <div class="abs delivery center-x">
      <div class="delivery-label">Order Delivery</div>
      <div class="delivery-phone">000 777 41936</div>
    </div>
    <div class="abs delivery-rule"></div>
    <div class="abs social" aria-label="Social links"><span></span><span></span><span></span></div>

    <div class="abs slider-shadow"></div>
    <div class="abs slider-frame"></div>
    <div class="abs slide" role="img" aria-label="Wicker basket of assorted fresh bread loaves on a lime green backdrop"></div>
    <svg class="abs slide-arrow" style="left:308px;top:255px" viewBox="0 0 27 27" aria-label="Previous slide">
      <circle cx="13.5" cy="13.5" r="13.5" fill="#b8cc1c"/>
      <path d="M15.5 9 L11 13.5 L15.5 18" fill="none" stroke="#4e5a02" stroke-width="2.5"/>
    </svg>
    <svg class="abs slide-arrow" style="left:830px;top:255px" viewBox="0 0 27 27" aria-label="Next slide">
      <circle cx="13.5" cy="13.5" r="13.5" fill="#b8cc1c"/>
      <path d="M11.5 9 L16 13.5 L11.5 18" fill="none" stroke="#4e5a02" stroke-width="2.5"/>
    </svg>

    <nav class="abs main-nav">
      <span>About Us</span><span>Contact Us</span><span>Frozen Yogurt</span><span>Toppings</span><span>Smoothies</span><span>Acai Bowls</span>
    </nav>
  </header>

  <section class="abs welcome-band">
    <div class="abs script-title center-x" style="left:579px;top:28px">Welcome</div>
    <div class="abs welcome-sub center-x" style="left:579px;top:52px">to our site</div>
    <div class="abs taster" style="left:424px;top:99px"><div class="taster-photo" role="img" aria-label="Dark grapes and yellow fruit on a pale table" style="background:radial-gradient(circle at 40% 45%,#4a3f5a,#8aa0a8 60%,#d8e2e2)"></div></div>
    <div class="abs taster" style="left:533px;top:99px"><div class="taster-photo" role="img" aria-label="Granola, seeds and lime on a dark board" style="background:radial-gradient(circle at 50% 50%,#9a7a58,#4d3a2c 65%,#2a2320)"></div></div>
    <div class="abs taster" style="left:642px;top:99px"><div class="taster-photo" role="img" aria-label="Sliced grapefruit and berries on grey stone" style="background:radial-gradient(circle at 55% 45%,#e07a6a,#b9b6b2 60%,#8e8c8a)"></div></div>
  </section>

  <section class="abs story-band">
    <div class="abs band-shadow" style="top:0"></div>
    <div class="abs script-title center-x" style="left:579px;top:42px">Yovella</div>
    <p class="abs copy" style="top:78px;margin:0">
      Yovella – yo.vel.la | noun a healthy and delicious frozen yogurt treat that sends your taste buds into a state of euphoria.<br>
      Nourish your body<span class="dot"></span>Treat others well<span class="dot"></span>Look after our planet
    </p>
    <div class="abs script-title center-x" style="left:579px;top:136px">Our features</div>
    <p class="abs copy" style="top:171px;margin:0">
      <strong>Delicious</strong>
      Our signature frozen yogurt is authentic. Using the freshest organic low fat milk, and fresh organic low fat yogurt. Giving you the best tasting yogurt experience.
      <strong>Nutritious</strong>
      98% fat free, live and active cultures with probiotics so only the best are being consumed.
      <strong>Conscious</strong>
      Our Acai range are organic and fair trade making sure we not only nourish our bodies with the best ingredients but we also conscious of people who have made our product are being looked after too.
    </p>
  </section>

  <footer class="abs site-footer">
    <div class="abs band-shadow" style="top:0"></div>
  </footer>
  <nav class="abs footer-nav">
    <span>About Us</span><span>Contact Us</span><span>Frozen Yogurt</span><span>Toppings</span><span>Smoothies</span><span>Acai Bowls</span>
  </nav>
</body>
</html>
```